Design Large Inspirational Artwork with Long Quote

Design a large piece of art with a quote from Marcus Tillwright.

QUOTE
"The thing that's so interesting about being alive is that you're all in. No matter what you do, you're all in. This is gonna kill you, so I think you might as well play the most magnificent game you can while you're waiting. Because, do you have anything better to do? Why not pick the best thing possible that you could do? Because you're more powerful than you think, way more powerful than you think. I mean, God only knows what you are in the final analysis. You're blind to your own weaknesses, but you're also blind to your own strengths. How far could you take that if you stopped wasting time, and if you stopped lying, and if you oriented yourself to the highest possible good that you could conceive of and you committed to that? How much good could you do? Well, I would say: why don't you find out?"

SIZE
A high-resolution print size of 6' wide and 3' tall should provide ample space for both the quote and the accompanying artwork.

TYPOGRAPHY
Choose a bold, clean, and easily readable font for the quote. You could also experiment with different font sizes for certain words or phrases to emphasize their importance within the quote.

COLORS
Since the quote is thought-provoking and reflective, you might want to use a color palette that evokes a sense of introspection and depth. Consider using cool, calming colors like shades of blue, gray, or green. Alternatively, you can use a contrasting color scheme with a light background and dark text to make the quote stand out.

ARTWORK
Select / create / edit background artwork to complement the quote.
While a great design might be minimalistic and/or greyscale, I'd really like to see some full color options. This might be anything from photography or graphics inspired by the ideas in the text, to abstract colors or illustrations that feel like the sentiment expressed.
The art should capture your attention and encourage you to read the text. The art should be visually appealing, both at a distance and up close, regardless of whether the text is read.
Updates

Having trouble confirming the exact print size.

Still looking for printing solution and final size confirmation.

Target Market(s)

Personal, business, office

Industry/Entity Type

None

Font styles to use
Sans Serif
Script

Requirements
Must have
• Entire quote, legible text, modern design, attractive artwork, approx 6ft wide and 3ft tall
Nice to have
• Different font (sizes) for certain words or phrases to emphasize their importance within the quote.

```html
<!DOCTYPE html>
<html lang="en">
<head>
<meta charset="utf-8">
<title>Marcus Tillwright – Why Don't You Find Out</title>
<link href="https://fonts.googleapis.com/css2?family=Jost:wght@300;400;500&family=Great+Vibes&family=Montserrat:wght@800;900&family=Fira+Sans:wght@600;700&family=Oswald:wght@600&family=Mulish:wght@800&display=swap" rel="stylesheet">
<style>
  :root{
    --ink:#111111;
    --sky-top:#dfeaf3;
    --sky-mid:#f4f8fb;
    --sky-low:#e7eef4;
    --blue:#1a9bd7;
    --blue-deep:#1565b4;
    --orange-red:#f15a29;
    --green-script:#0f7a45;
    --green:#3cb54a;
    --green-deep:#0d9346;
    --yellow:#f6c21a;
    --orange:#f7941d;
    --red:#e8202a;
    --crimson:#c8203a;
    --plum:#a3195b;
    --magenta:#d6185b;
    --purple:#6a2c91;
    --grey:#444444;
    --band:#a8a8a8;
    --circle-blue:#27a8e0;
    --circle-yellow:#ffe01b;
    --circle-green:#3cb54a;
    --sans:'Jost', sans-serif;
    --script:'Great Vibes', cursive;
  }
  html,body{margin:0;padding:0;overflow:hidden;}
  body{width:1200px;height:600px;}
  .artwork{
    position:relative;width:1200px;height:600px;overflow:hidden;box-sizing:border-box;margin:0;
    border:1px solid #222;
    background:
      radial-gradient(ellipse 420px 180px at 180px 90px, rgba(205,225,238,.9), transparent 70%),
      radial-gradient(ellipse 380px 200px at 1000px 300px, rgba(210,220,230,.7), transparent 70%),
      radial-gradient(ellipse 500px 160px at 300px 420px, rgba(255,255,255,.8), transparent 70%),
      linear-gradient(180deg,var(--sky-top) 0%,var(--sky-mid) 45%,var(--sky-low) 100%);
    font-family:var(--sans);color:var(--ink);
  }
  .line{position:absolute;left:0;width:1200px;text-align:center;white-space:nowrap;line-height:1;margin:0;}
  .script{font-family:var(--script);font-weight:400;}
  .l1{top:89px;font-size:20px;}
  .l1 .alive{font-family:var(--script);color:var(--blue);font-size:66px;line-height:0;vertical-align:-6px;margin:0 3px;}
  .l2{top:118px;font-size:28px;}
  .l2 .all-in{font-family:'Mulish',sans-serif;font-weight:800;color:var(--orange-red);font-size:33px;}
  .l3{top:153px;font-size:19.5px;}
  .l4{top:164px;font-size:43px;color:var(--green-script);left:10px;}
  .l5{top:206px;font-size:19px;}
  .l5 .em{font-family:'Fira Sans',sans-serif;font-weight:600;color:var(--green);}
  .l6{top:230px;font-size:19.5px;}
  .l6 .em{font-family:'Fira Sans',sans-serif;font-weight:600;color:var(--yellow);}
  .l7{top:252px;font-size:19px;font-weight:300;color:var(--crimson);}
  .l8{top:273px;font-size:25px;font-family:'Montserrat',sans-serif;font-weight:900;}
  .l9{top:303px;font-size:19px;}
  .l9 .em{font-family:'Mulish',sans-serif;font-weight:800;color:var(--blue-deep);}
  .l10{top:328px;font-size:19px;}
  .l10 .weak{color:var(--orange);}
  .l10 .strong{font-family:'Fira Sans',sans-serif;font-weight:600;color:var(--red);}
  .l11{top:356px;font-size:19px;font-weight:300;}
  .caps{font-family:'Oswald',sans-serif;font-weight:600;font-size:19px;letter-spacing:.2px;}
  .l11 .c1{color:var(--plum);} .l11 .c2{color:var(--magenta);}
  .l12{top:379px;font-size:19px;font-weight:300;}
  .l12 .c3{color:var(--purple);}
  .l13{top:408px;font-size:19px;font-family:'Fira Sans',sans-serif;font-weight:600;color:var(--green-deep);}
  .l14{top:432px;font-size:19px;font-family:'Fira Sans',sans-serif;font-weight:600;color:var(--green-deep);}
  .l15{top:444px;font-size:54px;color:var(--blue);}
  .attribution{position:absolute;left:846px;top:492px;margin:0;font-family:'Mulish',sans-serif;font-weight:800;font-size:14px;color:var(--grey);}
  .accents{position:absolute;left:0;top:0;}
</style>
</head>
<body>
<main class="artwork">
  <svg class="accents" width="1200" height="600" viewBox="0 0 1200 600">
    <defs>
      <linearGradient id="bandTone" x1="0" y1="0" x2="1" y2="0">
        <stop offset="0" stop-color="var(--band)" stop-opacity=".35"/>
        <stop offset="0.5" stop-color="var(--band)" stop-opacity=".25"/>
        <stop offset="1" stop-color="var(--band)" stop-opacity=".35"/>
      </linearGradient>
      <linearGradient id="portraitTone" x1="0" y1="0" x2="0" y2="1">
        <stop offset="0" stop-color="#5a5a5a"/>
        <stop offset="0.35" stop-color="#2a2a2a"/>
        <stop offset="1" stop-color="#151515"/>
      </linearGradient>
    </defs>
    <rect role="img" aria-label="Faint repeated grey script tagline running along the bottom edge"
          x="0" y="522" width="1200" height="58" rx="6" fill="url(#bandTone)"/>
  </svg>

  <p class="line l1">The thing that’s so interesting about <span class="alive">being alive</span> is that you’re all in.</p>
  <p class="line l2">No matter what you do, <span class="all-in">you’re all in.</span></p>
  <p class="line l3">This is gonna kill you, so I think you might as well</p>
  <p class="line l4 script">play the most magnificent game you can while you’re waiting.</p>
  <p class="line l5">Because, do you have anything <span class="em">better to do?</span></p>
  <p class="line l6">Why not <span class="em">pick the best thing possible</span> that you could do?</p>
  <p class="line l7">Because you’re more powerful than you think,</p>
  <p class="line l8">way more powerful than you think.</p>
  <p class="line l9">I mean, <span class="em">God only knows</span> what you are in the final analysis.</p>
  <p class="line l10">You’re <span class="weak">blind to your own weaknesses,</span> but you’re also <span class="strong">blind to your own strengths.</span></p>
  <p class="line l11">How far could you take that if you <span class="caps c1">STOPPED WASTING TIME,</span> and if you <span class="caps c2">STOPPED LYING,</span></p>
  <p class="line l12">and if you oriented yourself to the <span class="caps c3">HIGHEST POSSIBLE GOOD</span></p>
  <p class="line l13">that you could conceive of and you committed to that?</p>
  <p class="line l14">How much good could you do? Well, I would say:</p>
  <p class="line l15 script">why don’t you find out?</p>

  <p class="attribution">Marcus Tillwright.</p>

  <svg class="accents" width="1200" height="600" viewBox="0 0 1200 600">
    <circle cx="1113" cy="347" r="19" fill="var(--circle-blue)"/>
    <circle cx="1164" cy="416" r="32" fill="var(--circle-yellow)"/>
    <circle cx="1046" cy="475" r="75" fill="var(--circle-green)"/>
    <rect role="img" aria-label="Black and white portrait of the speaker in a dark suit, arms crossed"
          x="1028" y="386" width="140" height="214" rx="40" fill="url(#portraitTone)"/>
  </svg>
</main>
</body>
</html>
```